Brennick Holdings Business Cards

These are professional business cards that are for my family office.
Put fake emails and phone numbers as of now until I finalize those components. This family office controls my families investments, assets, and future. The cards should be professional.
..
.
.
.
I just uploaded another variation of a logo I would like to see as a business card to I am inbeteen which logo to use

Target Market(s)

business

Industry/Entity Type

business

Contact Information for Business Card

Professional, wealth related, finance related.

Requirements
Must have
• Logo

```html
<!DOCTYPE html>
<html lang="en">
<head>
<meta charset="utf-8">
<title>Brennick Holdings Business Cards</title>
<link href="https://fonts.googleapis.com/css2?family=Montserrat:wght@400;600;700&display=swap" rel="stylesheet">
<style>
  :root {
    --backdrop: #2f3033;
    --card: #ffffff;
    --navy: #1b1f2c;
    --text: #2a2d36;
  }
  * { margin: 0; padding: 0; box-sizing: border-box; }
  html, body { width: 1200px; height: 1059px; overflow: hidden; background: var(--backdrop); }
  body { font-family: "Montserrat", sans-serif; color: var(--text); position: relative; }

  .card {
    position: absolute;
    background: var(--card);
    border-radius: 22px;
    overflow: hidden;
    box-shadow: 0 12px 18px rgba(0,0,0,0.45);
  }
  .card--front { left: 256px; top: 100px; width: 688px; height: 392px; }
  .card--back  { left: 253px; top: 536px; width: 694px; height: 396px; }

  .brand-name {
    position: absolute;
    font-family: "Montserrat", sans-serif;
    font-weight: 600;
    color: var(--navy);
    text-transform: uppercase;
    letter-spacing: 1px;
    white-space: nowrap;
  }
  .card--front .brand-name { left: 27px; top: 34px; font-size: 28px; }
  .card--back .brand-name { left: 0; right: 0; top: 300px; text-align: center; font-size: 30px; }

  .brand-ring { position: absolute; }
  .card--front .brand-ring { left: 344px; top: 23px; }
  .card--back .brand-ring { left: 243px; top: 59px; }

  .name-marker {
    position: absolute; left: 0; top: 132px;
    width: 17px; height: 56px; background: var(--navy);
  }
  .holder-name {
    position: absolute; left: 27px; top: 128px;
    font-size: 31px; font-weight: 700; color: var(--navy); letter-spacing: 0.3px;
  }
  .holder-role {
    position: absolute; left: 27px; top: 166px;
    font-size: 18px; font-weight: 400; color: var(--text);
  }
  .address {
    position: absolute; left: 27px; top: 210px;
    font-size: 18px; line-height: 28px; font-style: normal;
  }
  .contact-list {
    position: absolute; left: 27px; top: 282px; list-style: none;
  }
  .contact-list li {
    display: flex; align-items: center; height: 27px; font-size: 18px;
  }
  .contact-list svg { width: 15px; height: 15px; margin-right: 9px; fill: var(--navy); }
</style>
</head>
<body>
  <section class="card card--front" aria-label="Business card front">
    <div class="brand-name">Brennick Holdings</div>
    <svg class="brand-ring" width="350" height="350" viewBox="0 0 350 350" aria-hidden="true">
      <circle cx="174" cy="174" r="169" fill="none" stroke="var(--navy)" stroke-width="5"/>
    </svg>
    <div class="name-marker"></div>
    <h1 class="holder-name">ADRIAN HALE</h1>
    <p class="holder-role">Managing Director</p>
    <address class="address">Your address, City<br>State, Zip 1234</address>
    <ul class="contact-list">
      <li>
        <svg viewBox="0 0 16 16" aria-hidden="true"><path d="M1 6c0-2 3-3 7-3s7 1 7 3v1h-3V5.5C10.5 5 5.5 5 4 5.5V7H1zM4 8h8l2 6H2z"/></svg>
        123 456 789
      </li>
      <li>
        <svg viewBox="0 0 16 16" aria-hidden="true"><path d="M1 4h14v1.2L8 9.5 1 5.2zM1 6.6l7 4.3 7-4.3V13H1z"/></svg>
        office@brennickmail.com
      </li>
      <li>
        <svg viewBox="0 0 16 16" aria-hidden="true"><circle cx="8" cy="8" r="7"/><path d="M4 4c2 0 3 1 2.5 2.5S4 8 5 10s2 2 1.5 4M10 2.5c0 2 1.5 2 2.5 3.5s0 3-1.5 4" fill="none" stroke="#fff" stroke-width="1.2"/></svg>
        www.brennickholdings.com
      </li>
    </ul>
  </section>

  <section class="card card--back" aria-label="Business card back">
    <svg class="brand-ring" width="218" height="218" viewBox="0 0 218 218" aria-hidden="true">
      <circle cx="109" cy="109" r="106" fill="none" stroke="var(--navy)" stroke-width="3.5"/>
    </svg>
    <div class="brand-name">Brennick Holdings</div>
  </section>
</body>
</html>
```